Velvet comb home studio

VELVET COMB.....at fox valley ,Wahroonga is a home hairdressing studio.
Hair services from a peaceful setting.
Quality colours and products.
free consultation prior to making appointment.
Easy and convenient after hours hair appointments.
Qualified hairdresser with over 15 years experience.
Specialise in foiling,balayage,ombre colour,tints,style cutting and blowdrying.
20 % off for new clients(colour services)
sms or call for 0491302667 for a quote.
Updates
im sorry guys but i has to re do alot of the photos. i would like something that looks elegant and classy.i will post an example of a flier style i like Added Wednesday, April 27, 2016
Project Deadline Extended Reason: im sorry i have decided i needed better photographs. please design again...i will choose someone before the deadline. please an elegant design will be great Added Wednesday, April 27, 2016
Target Market(s)
18-60 year olds
Industry/Entity Type
Hair
Requirements
Must have
- Must say home hairdressing studio
- Must say Velvet Comb at Fox Valley Wahroonga
- Must say phone number
Nice to have
- Modern but still classy and elegant
- Try to incorporate any photos which I have uploaded that looks best

```html
<!DOCTYPE html>
<html lang="en">
<head>
<meta charset="utf-8">
<title>Velvet Comb – Home hairdressing studio flyer</title>
<link rel="stylesheet" href="https://fonts.googleapis.com/css2?family=Tinos:ital,wght@1,400;1,700&family=Pinyon+Script&display=swap">
<style>
  :root {
    --page-bg: #ffffff;
    --ink: #1f1c1e;
    --ink-soft: #2c2729;
    --photo-warm: #e9d2bf;
    --photo-peach: #dcbfa8;
    --photo-veil: #e4e2e6;
    --photo-floor: #d9b28c;
    --shadow: rgba(0, 0, 0, 0.28);
  }
  * { margin: 0; padding: 0; box-sizing: border-box; }
  html, body {
    width: 1200px;
    height: 1014px;
    overflow: hidden;
    background: var(--page-bg);
  }
  .flyer {
    position: absolute;
    left: 114px;
    top: 144px;
    width: 1000px;
    height: 710px;
    overflow: hidden;
    font-family: "Tinos", "Times New Roman", serif;
    font-style: italic;
    font-weight: 400;
    color: var(--ink);
    box-shadow: 0 10px 30px var(--shadow);
  }
  .flyer__photo {
    position: absolute;
    inset: 0;
    background:
      linear-gradient(180deg, rgba(255,255,255,0) 72%, var(--photo-floor) 100%),
      linear-gradient(90deg, var(--photo-peach) 0%, var(--photo-warm) 18%, var(--photo-veil) 38%, var(--photo-veil) 62%, var(--photo-warm) 82%, var(--photo-peach) 100%);
  }
  .flyer__text {
    position: absolute;
    left: 0;
    width: 100%;
    text-align: center;
    white-space: nowrap;
    font-weight: 400;
    line-height: 1.2;
  }
  .studio-type { top: 71px; font-size: 32px; }
  .studio-name { top: 115px; font-size: 23px; }
  .studio-name__brand {
    font-family: "Pinyon Script", cursive;
    font-style: normal;
    font-size: 44px;
    margin-right: 6px;
  }
  .features {
    top: 212px;
    list-style: none;
    font-size: 19.4px;
    line-height: 28.8px;
    color: var(--ink-soft);
  }
  .offer__amount { top: 436px; font-size: 53px; }
  .offer__terms {
    top: 505px;
    font-family: "Pinyon Script", cursive;
    font-style: normal;
    font-size: 27px;
  }
  .contact { top: 597px; font-size: 25.5px; }
  .contact__phone { font-weight: 700; }
</style>
</head>
<body>
  <article class="flyer">
    <div class="flyer__photo" role="img" aria-label="Photo of a bright home salon room with French doors, a wall clock, a tall black mirror and a black styling chair on a timber floor"></div>

    <h1 class="flyer__text studio-type">Home hairdressing studio</h1>
    <p class="flyer__text studio-name"><span class="studio-name__brand">Velvet Comb</span>at Elm Ridge, Carrowbrook</p>

    <ul class="flyer__text features">
      <li>~ Hair services from a peaceful setting</li>
      <li>~ Quality colours and products</li>
      <li>~ Free consultation prior to making appointment</li>
      <li>~ Easy and convenient after hours hair appointments</li>
      <li>~ Qualified hairdresser with over 15 years experience</li>
      <li>~ Specialise in foiling,balayage,ombre colour,tints,style cutting and blowdrying</li>
    </ul>

    <p class="flyer__text offer__amount">20 % off</p>
    <p class="flyer__text offer__terms">for new clients(colour services)</p>

    <p class="flyer__text contact">sms or call <span class="contact__phone">0491302667</span> for a quote</p>
  </article>
</body>
</html>
```